(Wordpress)Website Design - No requirements! Sign Your name at the bottom of the site!

Dear Designer,

I am looking for a designer who is interested in a long-term business realtionship.
I already have 2 more designs to get done IMMEDIATELY after this website..
1.) An email brochure matching the website theme.
2.) A Billboard. BOTH MATCHING THE WEBSITE THEME

For this project, a bonus WILL be given.

Go to vaultnest.com as Site Inspiration

Please take this opportunity to design an existing wordpress website, FUNDSWIFTLANE.com, in whatever form your creativity takes you

I have no requirements other than a CREATIVE and OUT-OF -THE-BOX Design. Something Pretty and Eye Catching; a website that someone logs onto and doesnt want to leave

I have purchased a theme called velorant. You dont need to use it...But Info can be found at

http://skinbazaar.example/item/velorant-premium-wordpress-theme/full_screen_preview/482715

I have attached my logos and a PDF with a short story about what our company does.

Thank You,
-Tobin
PS I HAVE ANOTHER 2 DESIGNS TO DO AFTER THIS PROJECT.
also, IF YOU KNOW OF SOMEONE WHO DOES SEO WORK, I AM LOOKING FOR A FULL-TIME EMPLOYEE

Target Market(s)

Business Owners in a state of finacial NEED

Industry/Entity Type

Business

Requirements
Must have
• COLORFUL, EYE CATCHING

```html
<!DOCTYPE html>
<html lang="en">
<head>
<meta charset="utf-8">
<title>FundSwift Lane</title>
<link href="https://fonts.googleapis.com/css2?family=Source+Sans+3:wght@400;600;700&family=PT+Sans+Narrow:wght@400;700&family=Open+Sans:wght@400;600&display=swap" rel="stylesheet">
<style>
:root{
  --blue:#3d8ac4;
  --blue-dark:#2d6fa3;
  --blue-light:#5ea4d8;
  --charcoal:#4f4f4f;
  --ink:#2b2b2b;
  --muted:#777;
  --page:#eceeef;
  --white:#fff;
}
*{box-sizing:border-box;margin:0;padding:0}
html,body{width:993px;height:1200px;overflow:hidden}
body{
  position:relative;
  background:linear-gradient(180deg,#e4e7e9 0%,#f3f4f5 18%,#eef0f1 60%,#e6e8ea 100%);
  font-family:"Source Sans 3",sans-serif;color:var(--ink);
}
.abs{position:absolute}

/* header */
.brand{left:93px;top:24px;display:flex;align-items:center;gap:10px}
.brand-mark{width:34px;height:34px;border-radius:50%;background:var(--blue)}
.brand-name{font-size:34px;font-weight:600;color:var(--blue);letter-spacing:-.5px}
.login{left:629px;top:0;width:275px;height:89px;background:var(--charcoal);padding:20px 11px 0 11px;color:#fff}
.login-row{display:flex;gap:6px;align-items:center}
.login-field{height:17px;background:#fff;color:#222;font-size:9px;padding:2px 8px;width:97px}
.login-btn{height:17px;width:47px;background:var(--blue-light);font-size:9px;color:#fff;display:flex;align-items:center;justify-content:center;gap:3px}
.login-meta{display:flex;gap:14px;font-size:8px;margin-top:6px}
.login-meta .link{text-decoration:underline}
.login-call{font-size:12.5px;font-weight:600;margin-top:9px;text-align:center}

/* nav */
.main-nav{left:89px;top:132px;width:815px;height:34px;background:var(--blue)}
.nav-item{position:absolute;top:8px;font-size:14.5px;color:#fff;letter-spacing:-.3px}
.nav-item.active{background:var(--charcoal);padding:1px 9px;top:7px}

/* hero */
.hero{left:89px;top:209px;width:815px;height:297px;overflow:hidden;box-shadow:0 2px 5px rgba(0,0,0,.25)}
.hero-photo{position:absolute;inset:0;background:linear-gradient(90deg,#6d6660 0%,#b9b3ad 22%,#dcdcdc 45%,#cfd3cd 70%,#bfc6bd 100%)}
.hero-checks{position:absolute;left:315px;top:92px;list-style:none}
.hero-checks li{font-size:15px;letter-spacing:-.4px;height:23px;display:flex;align-items:center;gap:6px}
.hero-title{position:absolute;left:17px;top:198px;font-size:35px;font-weight:700;letter-spacing:-1.5px;color:#fff}
.hero-title span{color:var(--blue)}
.hero-sub{position:absolute;left:17px;top:237px;font-size:13px;line-height:19px;color:#fff;letter-spacing:-.3px}
.dot{position:absolute;top:276px;width:5px;height:5px;border-radius:50%;background:#444}
.dot.ring{width:8px;height:8px;background:none;border:1.5px solid #444;top:274px}

.apply-panel{left:626px;top:226px;width:294px;height:263px;background:linear-gradient(135deg,#3f90cc,#2f7fbd);box-shadow:0 2px 4px rgba(0,0,0,.3)}
.apply-input{position:absolute;left:14px;width:218px;height:26px;background:#fff;border:1px solid #cfd9e2;font-family:"PT Sans Narrow",sans-serif;font-size:8px;color:#777;padding:8px 9px}
.apply-vert{position:absolute;left:245px;top:235px;transform-origin:0 0;transform:rotate(-90deg);font-family:"Open Sans",sans-serif;font-size:33px;color:#fff;white-space:nowrap;letter-spacing:1px}
.apply-terms{position:absolute;left:18px;top:209px;font-family:"PT Sans Narrow",sans-serif;font-weight:700;font-size:14px;color:#fff;display:flex;align-items:center;gap:4px}
.apply-box{width:10px;height:10px;background:#fff}
.apply-submit{position:absolute;left:96px;top:232px;width:101px;height:23px;background:var(--charcoal);color:#fff;font-family:"PT Sans Narrow",sans-serif;font-weight:700;font-size:14px;display:flex;align-items:center;justify-content:center;gap:12px}
.fold{left:904px;top:489px}

/* banner */
.promo{left:89px;top:538px;width:815px;height:73px;background:var(--blue);text-align:center;color:#fff}
.promo-head{margin-top:6px;font-size:31px;font-weight:700;letter-spacing:-1.5px}
.promo-head span{font-family:"PT Sans Narrow",sans-serif;font-size:27px;letter-spacing:0}
.promo-sub{font-family:"Open Sans",sans-serif;font-size:18px;color:#111;margin-top:-4px}
.promo-shadow{left:140px;top:611px;width:713px;height:14px;background:radial-gradient(ellipse at top,rgba(0,0,0,.25),transparent 70%)}

/* steps */
.step-num{font-size:15px;font-weight:700;color:#555}
.step-label{font-size:16px;line-height:24px;color:#555;letter-spacing:-.5px}
.step-btn{width:100px;height:28px;display:flex;align-items:center;justify-content:center;color:#fff;font-size:15px;letter-spacing:-.5px;background:linear-gradient(#c4c4c4,#9a9a9a)}
.step-btn.primary{background:linear-gradient(#4f91c4,#2f6b9c)}
.divider{left:60px;top:783px;width:873px;height:3px;background:radial-gradient(ellipse,rgba(0,0,0,.18),transparent 70%)}

/* lower */
.section-head{height:37px;background:linear-gradient(90deg,var(--blue) 0%,var(--blue) 55%,rgba(61,138,196,0) 100%);font-family:"PT Sans Narrow",sans-serif;font-weight:700;font-size:24px;color:#fff;padding:5px 8px}
.section-head span{color:#8fb4d2}
.welcome-text{left:93px;top:866px;width:411px;font-family:"Open Sans",sans-serif;font-size:10.6px;line-height:23.2px;color:var(--muted);text-align:justify}
.testimonial{left:615px;top:867px;width:275px;height:128px;background:var(--charcoal);color:#fff;padding:0 18px 0 26px}
.quote{position:absolute;font-size:28px;font-family:Georgia,serif;color:#ddd}
.t-name{font-family:"Open Sans",sans-serif;font-size:20px;margin-top:22px}
.t-text{font-family:"Open Sans",sans-serif;font-size:8px;line-height:13.5px;margin-top:4px}
.subscribe-input{left:686px;top:1009px;width:137px;height:20px;background:#eee;border:1px solid #bbb;border-radius:3px;font-size:7.5px;font-style:italic;color:#666;padding:5px 7px}
.subscribe-btn{left:833px;top:1009px;width:49px;height:20px;background:linear-gradient(#7a8c99,#4f6270);border-radius:3px;color:#fff;font-family:"PT Sans Narrow",sans-serif;font-weight:700;font-size:10px;display:flex;align-items:center;justify-content:center}

.footer-nav{left:0;top:1108px;width:993px;display:flex;justify-content:center;font-size:10.5px;color:#444;letter-spacing:-.2px}
.footer-nav span{padding:0 10px;height:30px;line-height:18px;border-right:1px solid #bbb}
.footer-nav span:last-child{border-right:none}
</style>
</head>
<body>

<header>
  <div class="abs brand"><div class="brand-mark"></div><div class="brand-name">FundSwift Lane</div></div>
  <div class="abs login">
    <div class="login-row">
      <div class="login-field">Email:</div>
      <div class="login-field">Password</div>
      <div class="login-btn">&#9679; Login</div>
    </div>
    <div class="login-meta"><span>Keep me Logged in &#9634;</span><span class="link">Forgot your password</span></div>
    <div class="login-call">Begin Online Or Call Us Now! (800)555-0142</div>
  </div>
  <nav class="abs main-nav">
    <span class="nav-item active" style="left:223px">Home</span>
    <span class="nav-item" style="left:308px">About us</span>
    <span class="nav-item" style="left:401px">Services</span>
    <span class="nav-item" style="left:490px">FAQ'S</span>
    <span class="nav-item" style="left:567px">Our Advantage</span>
    <span class="nav-item" style="left:697px">Contact us</span>
  </nav>
</header>

<section class="abs hero">
  <div class="hero-photo" role="img" aria-label="Smiling businesswoman in an office with banknotes in the background"></div>
  <ul class="hero-checks">
    <li><svg width="14" height="14" viewBox="0 0 14 14"><path d="M1 7l4 5 8-11" fill="none" stroke="#555" stroke-width="2"/></svg>Instant Transfer</li>
    <li><svg width="14" height="14" viewBox="0 0 14 14"><path d="M1 7l4 5 8-11" fill="none" stroke="#555" stroke-width="2"/></svg>Instant Decision</li>
    <li><svg width="14" height="14" viewBox="0 0 14 14"><path d="M1 7l4 5 8-11" fill="none" stroke="#555" stroke-width="2"/></svg>Safe &amp; Secure</li>
    <li><svg width="14" height="14" viewBox="0 0 14 14"><path d="M1 7l4 5 8-11" fill="none" stroke="#555" stroke-width="2"/></svg>Choose Your Amount</li>
  </ul>
  <h1 class="hero-title"><span>APPLY</span> TODAY!</h1>
  <p class="hero-sub">For an instant capital with Line Feed<br>Apply in your web browser or on your cell phone</p>
  <span class="dot" style="left:384px"></span>
  <span class="dot" style="left:405px"></span>
  <span class="dot ring" style="left:423px"></span>
</section>

<form class="abs apply-panel">
  <div class="apply-input" style="top:15px">FIRST NAME:</div>
  <div class="apply-input" style="top:66px">LAST NAME</div>
  <div class="apply-input" style="top:117px">EMAIL</div>
  <div class="apply-input" style="top:169px">PHONE</div>
  <div class="apply-vert">APPLY NOW !</div>
  <div class="apply-terms"><span class="apply-box"></span>"I AGREE TO TERMS AND CONDITIONS"</div>
  <div class="apply-submit">SUBMIT <span>&#8250;</span></div>
</form>
<svg class="abs fold" width="16" height="16"><path d="M0 0h16L0 16z" fill="#264f70"/></svg>

<section class="abs promo">
  <div class="promo-head">No Credit Check ! <span>Be Up to $1,500 Richer in Less Than 1 Hour!</span></div>
  <div class="promo-sub">All you need is a checking account approval is guaranteed!</div>
</section>
<div class="abs promo-shadow"></div>

<section class="steps">
  <div class="abs step-num" style="left:118px;top:658px">1.</div>
  <svg class="abs" style="left:145px;top:654px" width="70" height="60" viewBox="0 0 70 60">
    <circle cx="34" cy="30" r="28" fill="#2f8fd6"/><circle cx="34" cy="30" r="22" fill="#e8f4fd"/>
    <path d="M34 30V14M34 30l-12 8" stroke="#2a6ea6" stroke-width="2.5"/>
  </svg>
  <div class="abs step-label" style="left:228px;top:657px">Apply For<br>Money</div>
  <div class="abs step-btn primary" style="left:204px;top:719px">Apply Now!</div>

  <div class="abs step-num" style="left:378px;top:658px">2.</div>
  <svg class="abs" style="left:412px;top:658px" width="56" height="56" viewBox="0 0 56 56">
    <circle cx="28" cy="28" r="26" fill="#2f8fd6"/>
    <path d="M15 28l9 9 17-18" fill="none" stroke="#fff" stroke-width="5" stroke-linecap="round"/>
  </svg>
  <div class="abs step-label" style="left:488px;top:657px">Get<br>Approved</div>
  <div class="abs step-btn" style="left:464px;top:719px">Apply Now!</div>

  <div class="abs step-num" style="left:631px;top:658px">3.</div>
  <div class="abs" style="left:665px;top:652px;width:52px;height:68px;background:linear-gradient(#bcd9ef,#3d8ac4)" role="img" aria-label="Businesswoman holding a money bag"></div>
  <div class="abs step-label" style="left:740px;top:657px">Receive<br>Your Money</div>
  <div class="abs step-btn" style="left:715px;top:719px">Apply Now!</div>
</section>
<div class="abs divider"></div>

<section>
  <h2 class="abs section-head" style="left:89px;top:814px;width:420px">Welcome to <span>FundSwift Lane</span></h2>
  <p class="abs welcome-text">Lorem Ipsum is simply dummy text of the printing and typesetting industry. Lorem Ipsum has been the industry's standard dummy text ever since the 1500s, when an unknown printer took a galley of type and scrambled it to make a type specimen book. It has survived not only five centuries, but also the leap into electronic typesetting, remaining essentially unchanged. It was popularised in the 1960s with the release of Typeleaf sheets containing Lorem Ipsum passages, and more recently with desktop publishing software like Pagecraft Studio including versions of Lorem Ipsum.</p>
</section>

<section>
  <h2 class="abs section-head" style="left:615px;top:814px;width:345px">Client Testimonials</h2>
  <svg class="abs" style="left:590px;top:928px" width="10" height="14"><path d="M8 1L2 7l6 6" fill="none" stroke="#aaa" stroke-width="2"/></svg>
  <svg class="abs" style="left:899px;top:928px" width="10" height="14"><path d="M2 1l6 6-6 6" fill="none" stroke="#aaa" stroke-width="2"/></svg>
  <blockquote class="abs testimonial">
    <span class="quote" style="left:5px;top:-2px">&ldquo;</span>
    <div class="t-name">Marcus Reyle</div>
    <p class="t-text">lacus, vel posuere felis. Curabitur bibendum vestibulum lorem, eget tempor piscing nisi. In congue justo a libero ullamcorper aliquet. Quisque gravida, justo ac tempor congue, nibh magna mattis felis, ut tempus ms. Integer sit amet.</p>
    <span class="quote" style="right:8px;top:96px">&rdquo;</span>
  </blockquote>
  <div class="abs subscribe-input">Enter your email to recive updates...</div>
  <div class="abs subscribe-btn">SUBSCRIBE</div>
</section>

<footer class="abs footer-nav">
  <span>Home</span><span>About us</span><span>Services</span><span>FAQ'S</span><span>Our Advantage</span><span>Contact us</span>
</footer>

</body>
</html>
```